Home care agency

Current website QRVCAREPLUS.com. Need to update and reformat to different pages. use my info from my current website

Target Market(s)

adult children

Industry/Entity Type

Home Health

Coding

Coded - Design and coding required

Number of Pages Required

4 page

Font styles to use
Sans Serif

Colors
3276b5
33a6d7
3277b5
85cae6
85acd3

```html
<!DOCTYPE html>
<html lang="en">
<head>
<meta charset="utf-8">
<title>QRV Care Plus Health Services</title>
<link href="https://fonts.googleapis.com/css2?family=Lato:wght@400;700&family=Libre+Baskerville:wght@400&display=swap" rel="stylesheet">
<style>
:root{
  --blue:#3276b5;
  --sky:#33a6d7;
  --light:#85cae6;
  --soft:#85acd3;
  --ink:#2e2e2e;
  --dark:#2b262b;
  --white:#fff;
}
*{box-sizing:border-box;margin:0;padding:0}
html,body{width:1200px;height:3626px;overflow:hidden}
body{position:relative;font-family:'Lato',sans-serif;color:var(--ink);background:var(--white)}
.abs{position:absolute}
.serif{font-family:'Libre Baskerville',serif}
.btn{position:absolute;background:var(--blue);color:#fff;border-radius:20px;display:flex;align-items:center;justify-content:center;font-size:13px}
/* top bar */
.topbar{top:0;left:0;width:1200px;height:32px;background:var(--sky);color:#fff;font-size:13px}
.topbar .social{right:0;top:0;width:290px;height:32px;background:var(--blue);clip-path:polygon(12% 0,100% 0,100% 100%,22% 100%)}
.dot{position:absolute;width:12px;height:12px;border-radius:50%;background:#fff}
/* header */
.header{top:32px;left:0;width:1200px;height:109px;background:#fff}
.brand-badge{position:absolute;left:78px;top:40px;width:108px;height:124px;border-radius:50% 50% 50% 50%/45% 45% 55% 55%;background:#fff;box-shadow:0 2px 6px rgba(0,0,0,.12);display:flex;align-items:center;justify-content:center;text-align:center;font-size:13px;color:var(--blue);z-index:2}
.brand-ring{width:96px;height:96px;border-radius:50%;border:3px solid var(--light);display:flex;align-items:center;justify-content:center;line-height:1.2}
.nav a{position:absolute;top:83px;font-size:13px;color:var(--ink);text-decoration:none}
.nav a.active{color:var(--sky)}
.nav a.active::after{content:"";position:absolute;left:0;right:0;top:24px;height:2px;background:var(--sky)}
/* hero */
.hero{top:141px;left:0;width:1200px;height:566px;background:linear-gradient(100deg,#3a2a1f 0%,#6b5240 35%,#8e7867 60%,#5d4a3e 100%)}
.hero h1{position:absolute;left:148px;top:225px;font-weight:400;font-size:30px;line-height:40px;color:#fff;letter-spacing:.5px}
/* about */
.section-title{font-weight:400;font-size:29px;color:var(--ink)}
.about p{position:absolute;left:122px;width:460px;font-size:12.5px;line-height:16px}
.about a{color:var(--blue);text-decoration:none}
.portrait{position:absolute;left:678px;top:798px;width:348px;height:348px;border-radius:50%;background:radial-gradient(circle at 50% 40%,#d7d9dc,#9aa7b3 60%,#6f7883);box-shadow:0 0 0 14px #eef4fa,0 0 0 30px #f7fafd}
/* skilled */
.skilled{top:1246px;left:0;width:1200px;height:560px;background:linear-gradient(180deg,#f5f5f6,#eeeff1)}
.ico{position:absolute;width:90px;height:90px;border-radius:50%;border:2px solid var(--blue);background:#fff;display:flex;align-items:center;justify-content:center}
.ico svg{width:50px;height:50px;stroke:var(--blue);fill:none;stroke-width:2}
.lbl{position:absolute;font-size:19px;line-height:23px;color:#333}
.center-mark{position:absolute;left:488px;top:1398px;width:222px;height:222px;border-radius:50%;border:5px dotted var(--soft);display:flex;align-items:center;justify-content:center;text-align:center;color:var(--blue);font-size:22px;line-height:1.3;background:#f3f4f5}
/* non medical */
.nonmed{top:1806px;left:0;width:600px;height:483px;background:var(--blue);color:#fff}
.nonmed-photo{top:1806px;left:600px;width:600px;height:483px;background:linear-gradient(120deg,#e8e4df,#c9c3bd 50%,#8c8f96)}
.nonmed li{list-style:none;position:absolute;left:118px;font-size:19px;display:flex;align-items:center;gap:16px}
.nonmed li svg{width:20px;height:20px;stroke:#fff;fill:none;stroke-width:2}
/* benefits */
.benefit{position:absolute;top:2428px;width:205px;height:205px;border-radius:50%}
.cap{position:absolute;top:2656px;width:240px;text-align:center;font-size:12.5px;line-height:16px;color:#444}
/* contact */
.contact-bg{top:2787px;left:0;width:1200px;height:451px;background:linear-gradient(90deg,#cfd3d8 0%,#dde0e3 40%,#b9c4cb 75%,#9fb8c2 100%)}
.card{position:absolute;left:120px;top:2843px;width:453px;height:350px;background:#fff}
.field{position:absolute;left:27px;width:401px;height:32px;border:1px solid #e2e2e2;font-size:13px;color:#555;padding:8px 11px}
/* footer */
.footer{top:3238px;left:0;width:1200px;height:333px;background:var(--dark);color:#fff}
.footer h4{position:absolute;font-weight:400;font-size:16px}
.footer h4::after{content:"";position:absolute;left:0;top:26px;width:40px;height:2px;background:var(--sky)}
.footer ul li{position:absolute;font-size:12.5px;list-style:disc}
.footer .line{position:absolute;font-size:12.5px;display:flex;gap:10px;align-items:center}
.footer .line svg{width:13px;height:13px;stroke:#ccc;fill:none;stroke-width:1.5}
.copy{top:3571px;left:0;width:1200px;height:55px;background:#fff;font-size:12.5px}
</style>
</head>
<body>

<div class="abs topbar">
  <div class="abs" style="left:80px;top:8px;display:flex;gap:8px;align-items:center">
    <svg width="15" height="11" viewBox="0 0 15 11" fill="none" stroke="#fff" stroke-width="1.4"><rect x="1" y="1" width="13" height="9"/><path d="M1 1l6.5 5 6.5-5"/></svg>+123 456 7890
  </div>
  <div class="abs" style="left:512px;top:8px;display:flex;gap:6px;align-items:center">
    <svg width="11" height="11" viewBox="0 0 12 12" fill="#fff"><path d="M2 1l3 0 1 3-1.5 1a7 7 0 003 3L9 6.5l3 1v3c0 .8-.7 1.2-1.5 1.2A10 10 0 01.8 2.5C.8 1.7 1.2 1 2 1z"/></svg>info@qrvcareplus.com
  </div>
  <div class="abs social">
    <span class="dot" style="left:98px;top:10px"></span>
    <span class="dot" style="left:144px;top:10px"></span>
    <span class="dot" style="left:190px;top:10px"></span>
    <span class="dot" style="left:236px;top:10px"></span>
  </div>
</div>

<div class="abs header">
  <nav class="nav">
    <a class="active" style="left:446px;top:51px">Home</a>
    <a style="left:520px;top:51px">About us</a>
    <a style="left:612px;top:51px">Services</a>
    <a style="left:700px;top:51px">Client Benefits</a>
    <a style="left:822px;top:51px">Contact us</a>
  </nav>
  <div class="btn" style="left:929px;top:38px;width:189px;height:37px">Employment Application</div>
</div>
<div class="brand-badge"><div class="brand-ring">QRV<br>Care Plus</div></div>

<section class="abs hero" role="img" aria-label="Photo of a smiling nurse in a white coat caring for a seated senior man in a living room">
  <h1 class="serif">Providing Care<br>Throughout the South Shore</h1>
  <div class="btn" style="left:153px;top:318px;width:197px;height:40px;font-size:13px">CARE INQUIRY FORM</div>
</section>

<section class="about">
  <h2 class="abs section-title serif" style="left:121px;top:795px">About us</h2>
  <span class="abs" style="left:122px;top:836px;width:84px;height:3px;background:var(--blue)"></span>
  <p style="top:865px">QRV Care Plus Health Services is owned and operated by Dana Whitfield. Dana is a registered nurse and has been in the health care system since 2001.</p>
  <p style="top:929px">&nbsp;She has specialized in home care, cardiology, trauma and critical care. She invests in future caregivers and has taught for the nursing programs at <a>Bayview University</a>, <a>Coastal Health Institute</a>, and <a>Seaside Nursing College</a>.</p>
  <p style="top:996px">All QRV Care Plus caregivers have extensive background checks and training regarding HIPAA compliance. We individualize the care of our clients in order to provide the best care possible in their home. QRV Care Plus also ensures full access and understanding of client care at all times with a caregiver binder in the client's home at all times.</p>
  <div class="btn" style="left:122px;top:1100px;width:158px;height:37px">Read More</div>
  <div class="portrait" role="img" aria-label="Portrait of the agency's founding nurse in a white coat"></div>
</section>

<section class="abs skilled">
  <h2 class="section-title serif" style="position:absolute;left:0;width:1200px;text-align:center;top:33px">Skilled Care Services</h2>
</section>
<div class="center-mark serif">QRV<br><span style="font-size:16px">Care Plus</span></div>

<div class="ico" style="left:384px;top:1336px"><svg viewBox="0 0 50 50"><rect x="12" y="9" width="24" height="32" rx="2"/><rect x="19" y="6" width="10" height="6"/><path d="M17 20h14M17 26h10M17 32h8M33 36l8-12"/></svg></div>
<div class="lbl" style="left:150px;top:1358px;width:212px;text-align:right">Free Initial Nursing<br>Assessment</div>

<div class="ico" style="left:724px;top:1336px"><svg viewBox="0 0 50 50"><path d="M14 36l16-16 4 4-16 16-6 2zM30 20l6-6M33 11l6 6M20 30l3 3"/></svg></div>
<div class="lbl" style="left:836px;top:1362px">Injections</div>

<div class="ico" style="left:336px;top:1457px"><svg viewBox="0 0 50 50"><rect x="14" y="14" width="22" height="28" rx="3"/><rect x="17" y="8" width="16" height="6"/><circle cx="25" cy="28" r="5"/><path d="M25 25v6M22 28h6"/></svg></div>
<div class="lbl" style="left:150px;top:1480px;width:168px;text-align:right">Medication<br>Management</div>

<div class="ico" style="left:770px;top:1457px"><svg viewBox="0 0 50 50"><circle cx="25" cy="17" r="7"/><path d="M12 42c0-9 6-14 13-14s13 5 13 14z"/><path d="M25 32v6M22 35h6"/></svg></div>
<div class="lbl" style="left:876px;top:1480px">Medical Care<br>Assistance</div>

<div class="ico" style="left:387px;top:1582px"><svg viewBox="0 0 50 50"><rect x="8" y="19" width="34" height="12" rx="6" transform="rotate(45 25 25)"/><rect x="8" y="19" width="34" height="12" rx="6" transform="rotate(-45 25 25)"/></svg></div>
<div class="lbl" style="left:262px;top:1620px">Wound Care</div>

<div class="ico" style="left:720px;top:1582px"><svg viewBox="0 0 50 50"><path d="M6 16h26v18H6zM32 22h7l5 6v6H32"/><circle cx="14" cy="36" r="3"/><circle cx="36" cy="36" r="3"/><path d="M19 21v8M15 25h8"/></svg></div>
<div class="lbl" style="left:828px;top:1603px">Transportation to<br>Medical Appointments</div>

<div class="ico" style="left:553px;top:1642px"><svg viewBox="0 0 50 50"><rect x="12" y="10" width="26" height="32" rx="2"/><path d="M20 16v8a5 5 0 0010 0v-8M25 29v5"/><circle cx="25" cy="36" r="2"/></svg></div>
<div class="lbl" style="left:0;width:1196px;text-align:center;top:1743px">Care Plan Management</div>

<section class="abs nonmed">
  <h2 class="serif" style="position:absolute;left:118px;top:81px;font-weight:400;font-size:29px">Non-Medical Services</h2>
  <ul>
    <li style="top:152px"><svg viewBox="0 0 20 20"><path d="M16 9v8H3V4h10"/><path d="M7 9l3 3 8-8"/></svg>Live-In Care</li>
    <li style="top:190px"><svg viewBox="0 0 20 20"><path d="M16 9v8H3V4h10"/><path d="M7 9l3 3 8-8"/></svg>Respite Care</li>
    <li style="top:228px"><svg viewBox="0 0 20 20"><path d="M16 9v8H3V4h10"/><path d="M7 9l3 3 8-8"/></svg>Assisting with Daily Living Activities</li>
    <li style="top:267px"><svg viewBox="0 0 20 20"><path d="M16 9v8H3V4h10"/><path d="M7 9l3 3 8-8"/></svg>Meal Preparations</li>
    <li style="top:305px"><svg viewBox="0 0 20 20"><path d="M16 9v8H3V4h10"/><path d="M7 9l3 3 8-8"/></svg>Companionship</li>
    <li style="top:343px"><svg viewBox="0 0 20 20"><path d="M16 9v8H3V4h10"/><path d="M7 9l3 3 8-8"/></svg>Homemaking</li>
  </ul>
</section>
<div class="abs nonmed-photo" role="img" aria-label="Photo of a caregiver helping a smiling senior man exercise with hand weights"></div>

<h2 class="abs section-title serif" style="left:0;width:1216px;text-align:center;top:2356px">Client Benefits</h2>
<div class="benefit" style="left:120px;background:linear-gradient(135deg,#c79a6e,#8a6a4e)" role="img" aria-label="Photo of a caregiver embracing a senior man outdoors"></div>
<div class="benefit" style="left:371px;background:linear-gradient(135deg,#9b8a5c,#d8d3c6)" role="img" aria-label="Photo of a senior man talking on the phone"></div>
<div class="benefit" style="left:622px;background:linear-gradient(135deg,#8a9db8,#c2785e)" role="img" aria-label="Photo of a family taking a photo with their grandfather"></div>
<div class="benefit" style="left:873px;background:linear-gradient(135deg,#e9e9ea,#b9bcc1)" role="img" aria-label="Photo of hands holding a payment card at a laptop"></div>
<div class="cap" style="left:102px">Continuity of care with same caregiver for each client on a regular basis.</div>
<div class="cap" style="left:353px">Open communication with owner by phone or email.</div>
<div class="cap" style="left:604px">Ongoing communications to client's family by phone or email on a weekly basis (if desired)</div>
<div class="cap" style="left:855px">Streamlined payment process.</div>

<section class="abs contact-bg" role="img" aria-label="Photo of a smiling senior woman with a caregiver's hands on her shoulders"></section>
<form class="card">
  <h2 class="serif" style="position:absolute;left:31px;top:21px;font-weight:400;font-size:24px">Contact us</h2>
  <div class="field" style="top:57px">Name*</div>
  <div class="field" style="top:94px">Phone*</div>
  <div class="field" style="top:131px">Email*</div>
  <div class="field" style="top:170px;height:99px">Message</div>
  <div class="btn" style="left:27px;top:285px;width:129px;height:30px">Send</div>
</form>

<footer class="abs footer">
  <div class="abs" style="left:141px;top:87px;width:154px;height:154px;border-radius:50%;background:#fff;display:flex;align-items:center;justify-content:center">
    <div class="serif" style="width:128px;height:128px;border-radius:50%;border:3px solid var(--light);display:flex;align-items:center;justify-content:center;text-align:center;color:var(--blue);font-size:17px;line-height:1.3">QRV<br>Care Plus</div>
  </div>
  <h4 class="serif" style="left:362px;top:70px">Quick Link</h4>
  <ul>
    <li style="left:381px;top:124px">Home</li>
    <li style="left:381px;top:148px">About us</li>
    <li style="left:381px;top:172px">Services</li>
    <li style="left:381px;top:196px">Client Benefits</li>
    <li style="left:381px;top:220px">Contact us</li>
  </ul>
  <h4 class="serif" style="left:570px;top:70px">Quick Contact</h4>
  <div class="line" style="left:570px;top:120px;align-items:flex-start"><svg viewBox="0 0 14 14"><path d="M7 13s-4.5-5-4.5-8a4.5 4.5 0 019 0c0 3-4.5 8-4.5 8z"/><circle cx="7" cy="5" r="1.5"/></svg><span style="line-height:26px;margin-top:-6px">480 Harbor Lane, Shoreline,<br>New York 11700, USA</span></div>
  <div class="line" style="left:570px;top:178px"><svg viewBox="0 0 14 14"><rect x="1" y="4" width="12" height="8"/><path d="M3 4V2h8v2"/></svg>(000)-555-0147</div>
  <div class="line" style="left:570px;top:203px"><svg viewBox="0 0 14 14"><rect x="1" y="3" width="12" height="8"/><path d="M1 3l6 5 6-5"/></svg>info@qrvcareplus.com</div>
  <h4 class="serif" style="left:832px;top:69px">Join Our Newletter</h4>
  <p class="abs" style="left:832px;top:121px;width:290px;font-size:12px;line-height:14px">Lorem Ipsum is simply dummy &nbsp;the printing and typesetting industry.</p>
  <div class="abs" style="left:830px;top:168px;width:285px;height:38px;border-radius:20px;background:#fff;color:#888;font-size:12px;font-style:italic;padding:12px 20px">Email Here</div>
  <div class="btn" style="left:830px;top:218px;width:285px;height:37px">Submit</div>
</footer>

<div class="abs copy">
  <span class="abs" style="left:119px;top:20px">Copyright © 2019 QRV Care Plus. All Right Reserved</span>
  <span class="abs" style="left:937px;top:16px;width:24px;height:24px;border-radius:50%;background:var(--blue)"></span>
  <span class="abs" style="left:977px;top:16px;width:24px;height:24px;border-radius:50%;background:var(--dark)"></span>
  <span class="abs" style="left:1016px;top:16px;width:24px;height:24px;border-radius:50%;background:var(--dark)"></span>
  <span class="abs" style="left:1055px;top:16px;width:24px;height:24px;border-radius:50%;background:var(--dark)"></span>
  <span class="abs" style="left:1094px;top:16px;width:24px;height:24px;border-radius:50%;background:var(--dark)"></span>
</div>

</body>
</html>
```